Business Card Design

We need a design for business cards for our company. We have a logo. We teach EMT's and we are based out of Virginia. The information that will need to add would be, name, title, phone number, email, address. On the back of the business card would be "We help you, help others"

Target Market(s)

People that want to become EMT's

Colors

Designer to choose colors to be used in the design.

Requirements
Must have
• company logo

```html
<!DOCTYPE html>
<html lang="en">
<head>
<meta charset="utf-8">
<title>Firstline Training – Business Card</title>
<link rel="stylesheet" href="https://fonts.googleapis.com/css2?family=Lato:wght@300;400;700;900&display=swap">
<style>
  :root {
    --stage: #1b1b1d;
    --card: #20263a;
    --card-deep: #181d2d;
    --card-glow: #2a3046;
    --red: #e8263f;
    --steel: #7d8794;
    --white: #f2f3f6;
    --muted: #aab1bf;
  }
  * { box-sizing: border-box; margin: 0; padding: 0; }
  html, body { width: 1200px; height: 900px; overflow: hidden; }
  body {
    background: var(--stage);
    font-family: "Lato", Arial, sans-serif;
    position: relative;
  }
  .card {
    position: absolute;
    left: 250px;
    width: 700px;
    height: 400px;
    overflow: hidden;
    background: linear-gradient(135deg, var(--card) 0%, var(--card-deep) 60%, var(--card) 100%);
    box-shadow: 0 18px 40px rgba(0,0,0,.55);
  }
  .card-back { top: 35px; }
  .card-front { top: 465px; }

  .accent-field {
    position: absolute;
    right: 0; top: 0;
    width: 300px; height: 100%;
    background: radial-gradient(ellipse at 70% 35%, var(--card-glow) 0%, rgba(42,48,70,0) 70%);
  }

  .stethoscope {
    position: absolute;
    left: 95px; top: 50px;
    width: 230px; height: 170px;
    border-radius: 40px;
    background: radial-gradient(ellipse at 45% 50%, #0d0f16 0%, #151926 55%, rgba(32,38,58,0) 100%);
  }

  .brand {
    display: flex;
    align-items: center;
    gap: 10px;
    color: var(--red);
    font-weight: 700;
    text-transform: uppercase;
    letter-spacing: .02em;
  }
  .brand-dot {
    width: 16px; height: 16px;
    border-radius: 50%;
    background: var(--red);
    flex: none;
  }
  .card-back .brand {
    position: absolute;
    left: 150px; top: 232px;
    font-size: 34px;
  }
  .tagline {
    position: absolute;
    left: 150px; top: 300px;
    color: var(--white);
    font-size: 24px;
    font-weight: 400;
    letter-spacing: .04em;
  }

  .card-front .brand {
    position: absolute;
    left: 190px; top: 90px;
    font-size: 40px;
  }

  .contact {
    position: absolute;
    left: 60px; top: 235px;
    color: var(--white);
  }
  .contact-name {
    font-size: 24px;
    color: var(--red);
    letter-spacing: .02em;
  }
  .contact-name .first { font-weight: 900; }
  .contact-name .last { font-weight: 300; }
  .contact-title {
    font-size: 15px;
    font-weight: 700;
    margin-top: 2px;
  }
  .contact-list { list-style: none; margin-top: 14px; }
  .contact-list li {
    display: flex;
    align-items: center;
    gap: 10px;
    font-size: 15px;
    line-height: 24px;
  }
  .contact-list svg { width: 14px; height: 14px; fill: var(--red); flex: none; }

  .edge-bands {
    position: absolute;
    left: 0; bottom: 0;
    width: 700px; height: 50px;
  }
</style>
</head>
<body>

  <section class="card card-back" aria-label="Card back">
    <div class="accent-field"></div>
    <div class="stethoscope" role="img" aria-label="Photograph of a black stethoscope"></div>
    <div class="brand"><span class="brand-dot"></span>Firstline Training</div>
    <p class="tagline">WE HELP YOU, HELP OTHERS</p>
  </section>

  <section class="card card-front" aria-label="Card front">
    <div class="accent-field"></div>
    <div class="brand"><span class="brand-dot"></span>Firstline Training</div>

    <div class="contact">
      <p class="contact-name"><span class="first">DANA</span> <span class="last">KESTER</span></p>
      <p class="contact-title">Founder / Director</p>
      <ul class="contact-list">
        <li>
          <svg viewBox="0 0 24 24" aria-hidden="true"><path d="M6.6 10.8a15.1 15.1 0 0 0 6.6 6.6l2.2-2.2a1 1 0 0 1 1-.25 11.4 11.4 0 0 0 3.6.57 1 1 0 0 1 1 1V20a1 1 0 0 1-1 1A17 17 0 0 1 3 4a1 1 0 0 1 1-1h3.5a1 1 0 0 1 1 1c0 1.25.2 2.45.57 3.57a1 1 0 0 1-.25 1z"/></svg>
          +1 540 555 0147
        </li>
        <li>
          <svg viewBox="0 0 24 24" aria-hidden="true"><path d="M2 5h20v14H2z M3.5 6.5 12 12.5l8.5-6" fill="var(--red)"/><path d="M3.5 6.5 12 12.5l8.5-6" fill="none" stroke="#20263a" stroke-width="1.6"/></svg>
          hello@firstlinetraining.com
        </li>
      </ul>
    </div>

    <svg class="edge-bands" viewBox="0 0 700 50" aria-hidden="true">
      <rect class="band-steel" x="0" y="36" width="700" height="14" fill="var(--steel)"/>
      <path class="band-red" d="M470 36 C470 24 478 18 492 18 L700 18 L700 36 Z" fill="var(--red)"/>
    </svg>
  </section>

</body>
</html>
```